Business Card Design

Divorce
Collaborative Family Law
Family Dispute Resolution
Family Law Property & Children

Target Market(s)

Australia

Industry/Entity Type

Business

Contact Information for Business Card

Delphine Hartwell
M App Law (Family Law) LLB (Hons) BA (Hons) Ass Dip Ag (HH)
Family Dispute Resolution Provider
Hartwell Family Law
PO Box 4723 Harkaway 3806
Phone 03 58217000 Fax 03 58217100 Email hartwellfamilylaw@quillnet.example

Colors
f04a51

Requirements
Should not have
• Any reference to
United States or US terminology
the word Company

```html
<!DOCTYPE html>
<html lang="en">
<head>
<meta charset="utf-8">
<title>Hartwell Family Law – Business Card</title>
<link rel="stylesheet" href="https://fonts.googleapis.com/css2?family=Tinos:wght@400&display=swap">
<style>
  :root {
    --backdrop: #e9e9ea;
    --card: #fbfbfb;
    --ink: #111111;
    --ink-soft: #444444;
    --accent: #f04a51;
    --wood-light: #c98a4e;
    --wood-dark: #7a4420;
    --robe: #2a2224;
    --window: #efe9e2;
    --shadow: rgba(0,0,0,0.18);
  }
  * { margin: 0; padding: 0; box-sizing: border-box; }
  html, body {
    width: 1200px; height: 864px; overflow: hidden;
    background: var(--backdrop);
  }
  .business-card {
    position: absolute; left: 75px; top: 132px;
    width: 1050px; height: 600px;
    background: var(--card);
    display: flex;
    box-shadow: 0 12px 36px var(--shadow);
    font-family: "Tinos", "Times New Roman", serif;
    color: var(--ink);
  }
  .card-photo {
    width: 470px; height: 100%;
    background:
      linear-gradient(180deg, transparent 0%, transparent 55%, var(--wood-light) 72%, var(--wood-dark) 100%),
      linear-gradient(100deg, var(--window) 0%, #b9a89a 30%, var(--robe) 62%, var(--robe) 100%);
  }
  .accent-rule {
    width: 8px; height: 100%;
    background: var(--accent);
  }
  .card-details {
    flex: 1; position: relative;
    padding: 72px 40px 0 62px;
  }
  .holder-name {
    font-size: 34px; letter-spacing: 2px; font-weight: 400;
    text-transform: uppercase;
  }
  .holder-credentials {
    margin-top: 8px; font-size: 15px; letter-spacing: 0.3px;
    color: var(--ink-soft);
  }
  .holder-title {
    margin-top: 6px; font-size: 18px; letter-spacing: 0.5px;
    color: var(--accent);
  }
  .holder-phone {
    margin-top: 14px; font-size: 22px; letter-spacing: 1px;
  }
  .contact-list {
    position: absolute; left: 62px; top: 355px;
    list-style: none; font-size: 23px; letter-spacing: 0.5px;
  }
  .contact-item {
    display: flex; align-items: flex-start; margin-bottom: 14px;
  }
  .contact-icon {
    width: 24px; height: 24px; margin-right: 22px; margin-top: 2px;
    flex-shrink: 0; fill: var(--ink);
  }
  .contact-text { line-height: 1.3; }
</style>
</head>
<body>
  <article class="business-card">
    <div class="card-photo" role="img" aria-label="Photograph of a wooden judge's gavel striking its block on a courtroom bench"></div>
    <div class="accent-rule"></div>
    <section class="card-details">
      <h1 class="holder-name">Delphine Hartwell</h1>
      <p class="holder-credentials">M App Law (Family Law) LLB (Hons) BA (Hons) Ass Dip Ag (HH)</p>
      <p class="holder-title">Family Dispute Resolution Provider</p>
      <p class="holder-phone">03 58217000</p>
      <ul class="contact-list">
        <li class="contact-item">
          <svg class="contact-icon" viewBox="0 0 24 24" aria-hidden="true"><path d="M12 2 1 12h3v9h6v-6h4v6h6v-9h3z"/></svg>
          <span class="contact-text">Hartwell Family Law<br>PO Box 4723 Harkaway 3806</span>
        </li>
        <li class="contact-item">
          <svg class="contact-icon" viewBox="0 0 24 24" aria-hidden="true"><path d="M2 5h20v14H2z M3.5 6.5 12 13l8.5-6.5" fill="none" stroke="#111" stroke-width="2"/><path d="M3 18 9.5 11.5M21 18l-6.5-6.5" stroke="#111" stroke-width="1.6"/></svg>
          <span class="contact-text">hartwellfamilylaw@quillnet.example</span>
        </li>
        <li class="contact-item">
          <svg class="contact-icon" viewBox="0 0 24 24" aria-hidden="true"><path d="M6 2h12v5H6z M2 8h20v9h-4v-3H6v3H2z M7 15h10v7H7z"/></svg>
          <span class="contact-text">03 58217100</span>
        </li>
      </ul>
    </section>
  </article>
</body>
</html>
```